Business Card Design Project

Name of Company: Barwinek Coaching & Consulting
Possible Acronym: BC&C
My Name: Lorelei Barwinek, LL.B.
My email address: lorelei@barwinekconsulting.example
My tel.: +44 (0) 7834 629 058
My skype address: barwinekbc
I am offering executive coaching and consulting in the area of business development and strategic planning to intellectual property law firms around the world.
Since I will be marketing to the legal industry, the card must be fairly conservative. However I want it to also have flare and spark. I want to convey to potential clients that I can be the spark that will ignite their potential. I like the combination of navy blue and hot pink. However, I have decided that hot pink is not corporate enough so I would like to use a colour with navy that comes close to hot pink but is more conservative. Not red. I would consider swapping navy blue for grey if you thought that would look better. I would like the background of the card to be entirely white - both back and front - only the letters will be in colour.
I would like the card to be double sided with the name of my firm (or the acronym) and my email address underneath (lorelei@barwinekconsulting.example) on the back and on the front, all of the information above.
With gratitude!
Lorelei

```html
<!DOCTYPE html>
<html lang="en">
<head>
<meta charset="utf-8">
<title>Barwinek Coaching &amp; Consulting — Business Card Back</title>
<link rel="stylesheet" href="https://fonts.googleapis.com/css2?family=PT+Sans:wght@400;700&display=swap">
<style>
  :root {
    --card-white: #ffffff;
    --brand-navy: #232a8c;
    --brand-rose: #f0173f;
  }
  html, body {
    margin: 0;
    padding: 0;
    width: 1200px;
    height: 686px;
    overflow: hidden;
    background: var(--card-white);
  }
  .card {
    position: relative;
    width: 1200px;
    height: 686px;
    background: var(--card-white);
  }
  .card__firm-name {
    position: absolute;
    left: 0;
    right: 0;
    top: 270px;
    margin: 0;
    text-align: center;
    font-family: "PT Sans", Tahoma, sans-serif;
    font-weight: 700;
    font-size: 64px;
    line-height: 1;
    letter-spacing: 0.5px;
    color: var(--brand-navy);
  }
  .card__email {
    position: absolute;
    left: 0;
    right: 0;
    top: 372px;
    margin: 0;
    text-align: center;
    font-family: "PT Sans", Tahoma, sans-serif;
    font-weight: 400;
    font-size: 48px;
    line-height: 1;
    color: var(--brand-rose);
  }
</style>
</head>
<body>
  <main class="card">
    <h1 class="card__firm-name">Barwinek Coaching &amp; Consulting</h1>
    <p class="card__email">lorelei@barwinekconsulting.example</p>
  </main>
</body>
</html>
```